Very clean, very simple business card needed.

I am looking for a VERY simple business card. I have attached our logo. I would like it to be a mainly white card. I have picked double sided but would be open to single as well. I want the overall feel to be simple, classic, and professional. Thank you.

Industry/Entity Type

Consultant

Contact Information for Business Card

Dennis Pellowe

862 North Larchmere Avenue, Summit Floor, Brennick Falls, Norland 60719
denny@hollisterbaycapital.example
www.hollisterbaycapital.example

Font styles to use
Serif

Colors

Designer to choose colors to be used in the design.

Requirements
Must have
• The business card details and in an editable form to change the names and emails of employees easily.
Nice to have
• n/a
Should not have
• Pictures, big lines and stripes, too much color.

```html
<!DOCTYPE html>
<html lang="en">
<head>
<meta charset="utf-8">
<title>Hollister Bay Capital – Business Card</title>
<link href="https://fonts.googleapis.com/css2?family=Raleway:wght@400;500&display=swap" rel="stylesheet">
<style>
  :root {
    --backdrop: #1c1d21;
    --card: #ffffff;
    --ink: #2b5177;
    --ink-soft: #3d6389;
  }
  * { box-sizing: border-box; margin: 0; padding: 0; }
  html, body {
    width: 1200px;
    height: 900px;
    overflow: hidden;
    background: var(--backdrop);
    font-family: "Raleway", sans-serif;
  }
  .stage {
    position: relative;
    width: 1200px;
    height: 900px;
  }
  .card {
    position: absolute;
    width: 525px;
    height: 300px;
    background: var(--card);
    color: var(--ink);
  }
  .card--back { left: 50px; top: 300px; }
  .card--front { left: 625px; top: 300px; }

  .brand {
    display: flex;
    align-items: center;
    gap: 12px;
  }
  .brand__mark {
    width: 22px;
    height: 22px;
    background: var(--ink);
    flex: none;
  }
  .brand__name {
    font-weight: 500;
    font-size: 21px;
    letter-spacing: 1.5px;
    text-transform: uppercase;
    color: var(--ink);
    white-space: nowrap;
  }
  .card--front .brand {
    position: absolute;
    left: 50%;
    top: 50%;
    transform: translate(-50%, -50%);
  }
  .card--back .brand {
    position: absolute;
    right: 30px;
    top: 96px;
  }
  .card--back .brand__name { font-size: 17px; letter-spacing: 1.2px; }
  .card--back .brand__mark { width: 18px; height: 18px; }

  .contact {
    position: absolute;
    left: 34px;
    top: 150px;
    color: var(--ink-soft);
  }
  .contact__name {
    font-size: 17px;
    font-weight: 500;
    color: var(--ink);
    margin-bottom: 6px;
    padding-left: 18px;
  }
  .contact__line {
    display: flex;
    align-items: flex-start;
    gap: 6px;
    font-size: 12px;
    line-height: 16px;
  }
  .contact__line svg { flex: none; margin-top: 2px; }
  .contact__text { display: block; white-space: nowrap; }
</style>
</head>
<body>
<main class="stage">

  <section class="card card--back" aria-label="Card back with contact details">
    <div class="brand">
      <span class="brand__mark"></span>
      <span class="brand__name">Hollister Bay Capital</span>
    </div>

    <div class="contact">
      <p class="contact__name">Dennis Pellowe</p>
      <p class="contact__line">
        <svg width="12" height="12" viewBox="0 0 12 12" aria-hidden="true">
          <path d="M6 1a3.5 3.5 0 0 0-3.5 3.5C2.5 7.2 6 11 6 11s3.5-3.8 3.5-6.5A3.5 3.5 0 0 0 6 1z" fill="var(--ink)"/>
          <circle cx="6" cy="4.5" r="1.3" fill="#fff"/>
        </svg>
        <span class="contact__text">862 North Larchmere Avenue, Summit Floor,<br>Brennick Falls, Norland 60719</span>
      </p>
      <p class="contact__line">
        <svg width="12" height="12" viewBox="0 0 12 12" aria-hidden="true">
          <rect x="1" y="2.5" width="10" height="7" fill="none" stroke="var(--ink)" stroke-width="1.1"/>
          <path d="M1 2.5l5 4 5-4" fill="none" stroke="var(--ink)" stroke-width="1.1"/>
        </svg>
        <span class="contact__text">denny@hollisterbaycapital.example</span>
      </p>
      <p class="contact__line">
        <svg width="12" height="12" viewBox="0 0 12 12" aria-hidden="true">
          <circle cx="6" cy="6" r="4.8" fill="none" stroke="var(--ink)" stroke-width="1.1"/>
          <ellipse cx="6" cy="6" rx="2" ry="4.8" fill="none" stroke="var(--ink)" stroke-width="0.9"/>
          <path d="M1.2 6h9.6" stroke="var(--ink)" stroke-width="0.9"/>
        </svg>
        <span class="contact__text">www.hollisterbaycapital.example</span>
      </p>
    </div>
  </section>

  <section class="card card--front" aria-label="Card front">
    <div class="brand">
      <span class="brand__mark"></span>
      <span class="brand__name">Hollister Bay Capital</span>
    </div>
  </section>

</main>
</body>
</html>
```